Walk Bold Stay Kind Ebook and Print book cover

I need a professional, eye catching cover that will stand out. The title of the book is "Walk Bold Stay Kind: 47 Quiet Rules For Calm and Wonder" It is a self-help personal transformation book by author Dale Ormsby. The cover will be on both print and ebook covers. I want something that is similar yet different to best-selling books in the genre, nothing too boring. A blue background might work, but it isn't a requirement. I'm open to other colors as long as it's powerful, professional, and screams "Buy me because this book is going to change your life!"
Updates

So far, 3 designs (3 of the 4 star rated designs) are in contention, but they all can be improved. I think the book cover should best convey "thinking smart" in a dynamic way. I'll run another poll in a day or so when I get additional designs I like. Added Thursday, May 4, 2017

Based on current designs, I wanted to provide additional guidance. The title and image should pop and be clearly visible at a distance as a thumbnail. Also, I'm wanting something bold and creative but not too confusing. I currently have a couple solid designs that are in contention to win, but I have another 7 days left for the project. I extended it to 10 days from the initial 5. I'll include several more polls for my followers and will likely pick the top ranking design based off the series of polls and will be eliminating lower ranking designs with each new poll and set of promising designs that come in. Finally, I may ask to see what the back will look like on the print version since I'll need both the Lumora and print (5" by 8") designs. Added Saturday, May 6, 2017

It's been recommended by some that I should have my own picture on the cover. I'm not completely convinced, but I would like to see some additional designs that incorporate my photo (touched up to remove the shine from my forehead and the label brand name removed from the t-shire) into a cover design. I have several good designs coming in, so typeset and professional looking font is extremely important. Blue is also preferred but not required. I've attached the photo on the brief for those who want to submit a design with that photo. Added Saturday, May 6, 2017

Target Market(s)

Working age adults seeking personal transformation and self improvement.

Industry/Entity Type

Motivation

Requirements
Must have
• Creativity. Eye catching. Striking. Contrast. Looks good close up and as a thumbnail at a distance. Font should be easy to read and pop from the cover along with the design.
Nice to have
• Powerful image placement. Play up the "Walk Bold" aspect of the title. Perhaps even contrasting someone who's thinking "Hard." Here are a few examples of intriguing covers (though not necessarily related to the genre) I like mainly for aesthetics and creativity. https://www.shopvale.com/dp/Q71MRT2KWD/ https://www.shopvale.com/dp/Q34PLN8XEA
• https://www.shopvale.com/dp/Q925GHV3TC/
• https://www.shopvale.com/dp/Q48DJW6RZB/
• (the font is a little poor in the last one but the image is evoking)
Should not have
• Ugly, tacky, or hard to read fonts. A simple photo with text on top. A simple background with words. Confusing images. Designs with no additional stock image purchase requirements will be given preference over those that do. I've seen a lot of balloons and light bulbs. I'm not saying you can't include them in the design, but if you want to stand out, try to find something more creative that expresses the concept of the title.

```html
<!DOCTYPE html>
<html lang="en">
<head>
<meta charset="utf-8">
<title>Walk Bold Stay Kind: 47 Quiet Rules For Calm and Wonder — Dale Ormsby</title>
<link rel="stylesheet" href="https://fonts.googleapis.com/css2?family=Fredoka:wght@600;700&family=Fjalla+One&family=Russo+One&display=swap">
<style>
  :root {
    --page: #ffffff;
    --cover-blue: #1f86d3;
    --cover-blue-deep: #1667b4;
    --cloud: #ffffff;
    --navy: #1c2c5c;
    --orange: #f07d22;
    --band: #e97a28;
    --cream: #f8ebc0;
    --sky: #3fc3f2;
    --heart: #f4a7a3;
    --author: #dcdff2;
    --author-shadow: #3a2a28;
    --brain-light: #f3a14a;
    --brain-mid: #e2643a;
    --brain-dark: #b8323a;
  }
  * { margin: 0; padding: 0; box-sizing: border-box; }
  html, body { width: 1200px; height: 1137px; overflow: hidden; background: var(--page); }
  .canvas { position: relative; width: 1200px; height: 1137px; }

  .cover {
    position: absolute; left: 321px; top: 28px; width: 558px; height: 1080px;
    overflow: hidden;
    background:
      repeating-linear-gradient(180deg, rgba(255,255,255,0.05) 0 2px, transparent 2px 7px),
      linear-gradient(160deg, var(--cover-blue) 0%, var(--cover-blue-deep) 100%);
  }
  .cover-shapes { position: absolute; inset: 0; }

  .title {
    position: absolute; left: 0; top: 0; width: 558px; height: 410px;
    font-family: "Fredoka", sans-serif; font-weight: 700; line-height: 1;
  }
  .title span { position: absolute; white-space: nowrap; }
  .title-walk { left: 150px; top: 50px; font-size: 88px; color: var(--navy); letter-spacing: 2px; }
  .title-bold { left: 238px; top: 145px; font-size: 96px; color: var(--orange); }
  .title-stay { left: 176px; top: 262px; font-size: 50px; color: var(--navy); }
  .title-kind { left: 290px; top: 255px; font-size: 96px; color: var(--orange); }

  .rule-count {
    position: absolute; left: 326px; top: 470px; width: 62px; height: 58px;
    font-family: "Fjalla One", sans-serif; font-size: 38px; color: var(--navy);
    text-align: center; line-height: 58px;
  }
  .subtitle-lead {
    position: absolute; left: 232px; top: 540px; width: 280px; text-align: center;
    font-family: "Fjalla One", sans-serif; font-size: 44px; color: var(--cream);
  }
  .subtitle-tail {
    position: absolute; left: 253px; top: 640px; width: 242px; text-align: center;
    font-family: "Fjalla One", sans-serif; color: #ffffff; line-height: 1.2;
  }
  .subtitle-tail .small { display: block; font-size: 34px; }
  .subtitle-tail .word { display: block; font-size: 38px; letter-spacing: 1px; }

  .author-band {
    position: absolute; left: 0; bottom: 0; width: 558px; height: 99px;
    background: var(--band);
    display: flex; align-items: center; justify-content: center;
  }
  .author-name {
    font-family: "Russo One", sans-serif; font-size: 58px; letter-spacing: 3px;
    color: var(--author); text-shadow: 3px 3px 0 var(--author-shadow);
  }
</style>
</head>
<body>
<div class="canvas">
  <div class="cover">
    <svg class="cover-shapes" width="558" height="1080" viewBox="0 0 558 1080">
      <defs>
        <linearGradient id="brain-tones" x1="0" y1="0" x2="0.4" y2="1">
          <stop offset="0" stop-color="var(--brain-light)"/>
          <stop offset="0.5" stop-color="var(--brain-mid)"/>
          <stop offset="1" stop-color="var(--brain-dark)"/>
        </linearGradient>
      </defs>
      <g class="title-cloud" fill="var(--cloud)">
        <ellipse cx="300" cy="110" rx="190" ry="100"/>
        <ellipse cx="180" cy="200" rx="110" ry="95"/>
        <ellipse cx="440" cy="150" rx="120" ry="110"/>
        <ellipse cx="250" cy="320" rx="140" ry="85"/>
        <ellipse cx="430" cy="310" rx="125" ry="95"/>
        <ellipse cx="330" cy="240" rx="180" ry="120"/>
        <circle cx="84" cy="314" r="21"/>
        <circle cx="66" cy="354" r="11"/>
      </g>
      <path class="heart" fill="var(--heart)" d="M59 218 L44 190 C30 178 28 158 42 152 C52 148 58 156 59 162 C60 154 68 146 78 150 C92 156 88 178 74 190 Z"/>
      <ellipse class="brain-art" role="img" aria-label="Watercolour illustration of one half of a brain in orange, pink and red"
               cx="30" cy="625" rx="190" ry="310" fill="url(#brain-tones)"/>
      <ellipse cx="357" cy="499" rx="32" ry="29" fill="var(--cream)"/>
      <path d="M337 520 L327 540 L351 526 Z" fill="var(--cream)"/>
      <ellipse cx="374" cy="728" rx="116" ry="128" fill="var(--sky)" stroke="var(--navy)" stroke-width="4"/>
      <circle cx="300" cy="905" r="17" fill="var(--sky)" stroke="var(--navy)" stroke-width="3"/>
      <circle cx="278" cy="938" r="8" fill="var(--sky)" stroke="var(--navy)" stroke-width="2"/>
    </svg>

    <h1 class="title">
      <span class="title-walk">WALK</span>
      <span class="title-bold">BOLD</span>
      <span class="title-stay">Stay</span>
      <span class="title-kind">KIND</span>
    </h1>

    <div class="rule-count">47</div>
    <div class="subtitle-lead">Quiet Rules</div>
    <div class="subtitle-tail">
      <span class="small">For</span>
      <span class="word">CALM</span>
      <span class="small">and</span>
      <span class="word">WONDER</span>
    </div>

    <div class="author-band">
      <span class="author-name">DALE ORMSBY</span>
    </div>
  </div>
</div>
</body>
</html>
```